Harrowdene Farm Lamb Sticker Design

We need to create a design for sticky labels that will be placed meat packaging of individual cuts of meat for Harrowdene Farm Lamb.

These sticke...

Target Market(s)

People who purchase Gourmet Meat Products. Higher income, Age 35-65

Industry/Entity Type

Farming

Requirements
Must have
• The Harrowdene Farm Lamb Logo (attached)
• Quality Grass Fed Lamb
• Need to create a look of premium quality product.
• Space to write Net Weight
• Space to write $

```html
<!DOCTYPE html>
<html lang="en">
<head>
<meta charset="utf-8">
<title>Harrowdene Farm Lamb – Leg Roast Label</title>
<link href="https://fonts.googleapis.com/css2?family=Oswald:wght@400;500;700&display=swap" rel="stylesheet">
<style>
  :root {
    --page: #ffffff;
    --brand-green: #0b9444;
    --label-cream: #f3f1ec;
    --ink: #1c1c1c;
  }
  html, body {
    margin: 0;
    padding: 0;
    width: 1200px;
    height: 730px;
    overflow: hidden;
    background: var(--page);
  }
  .canvas {
    position: relative;
    width: 1200px;
    height: 730px;
  }
  .label {
    display: block;
    width: 1200px;
    height: 730px;
    font-family: "Oswald", "Arial Narrow", sans-serif;
  }
  .label-body { filter: drop-shadow(0 14px 12px rgba(0,0,0,0.22)); }
  .frame-outer { fill: var(--brand-green); }
  .frame-panel { fill: var(--label-cream); }
  .frame-inner { fill: none; stroke: var(--brand-green); stroke-width: 2.4; }
  .headline { fill: var(--brand-green); font-weight: 700; font-size: 82px; }
  .rule-green { fill: var(--brand-green); }
  .rule-ink { fill: var(--ink); }
  .cut-name { fill: var(--ink); font-weight: 700; font-size: 58px; }
  .field-label { fill: var(--ink); font-weight: 500; font-size: 30px; }
  .field-label--large { font-weight: 700; font-size: 52px; }
  .field-label--small { font-size: 26px; }
  .currency { fill: var(--ink); font-weight: 700; font-size: 86px; }
  .brand-ring { fill: none; stroke: var(--ink); stroke-width: 6; }
  .brand-name { fill: var(--ink); font-weight: 700; font-size: 40px; text-anchor: middle; }
</style>
</head>
<body>
<main class="canvas">
  <svg class="label" viewBox="0 0 1200 730" xmlns="http://www.w3.org/2000/svg" role="group" aria-label="Harrowdene Farm Lamb leg roast label">
    <g class="label-body">
      <rect class="frame-outer" x="60" y="170" width="1088" height="390" rx="40"/>
      <rect class="frame-panel" x="71" y="181" width="1066" height="368" rx="30"/>
    </g>
    <rect class="frame-inner" x="80" y="194" width="1052" height="340" rx="24"/>

    <g class="brand">
      <circle class="brand-ring" cx="258" cy="370" r="142"/>
      <text class="brand-name" x="258" y="340">HARROWDENE</text>
      <text class="brand-name" x="258" y="390">FARM</text>
      <text class="brand-name" x="258" y="440">LAMB</text>
    </g>

    <text class="headline" x="438" y="302" textLength="662" lengthAdjust="spacingAndGlyphs">QUALITY GRASS FED LAMB</text>
    <rect class="rule-green" x="438" y="312" width="662" height="5"/>
    <rect class="rule-green" x="438" y="323" width="662" height="2.5"/>

    <text class="cut-name" x="440" y="388" textLength="170" lengthAdjust="spacingAndGlyphs">LEG ROAST</text>
    <rect class="rule-ink" x="750" y="344" width="3" height="50"/>
    <text class="field-label" x="770" y="388" textLength="125" lengthAdjust="spacingAndGlyphs">Sell by date</text>
    <rect class="rule-ink" x="438" y="399" width="662" height="2.5"/>

    <text class="field-label field-label--large" x="442" y="460" textLength="50" lengthAdjust="spacingAndGlyphs">Net.</text>
    <text class="field-label field-label--small" x="442" y="497" textLength="56" lengthAdjust="spacingAndGlyphs">Weight</text>

    <rect class="rule-ink" x="597" y="418" width="3" height="84"/>
    <text class="currency" x="636" y="494" textLength="36" lengthAdjust="spacingAndGlyphs">$</text>
    <text class="field-label" x="678" y="444" textLength="82" lengthAdjust="spacingAndGlyphs">Unit Price</text>

    <rect class="rule-ink" x="853" y="418" width="3" height="84"/>
    <text class="currency" x="896" y="494" textLength="36" lengthAdjust="spacingAndGlyphs">$</text>
    <text class="field-label" x="938" y="444" textLength="92" lengthAdjust="spacingAndGlyphs">Total Price</text>
  </svg>
</main>
</body>
</html>
```